HomeBridle business card and stationary design

We are looking for a simple yet elegant design for our mortgage company business card and stationary.

The card should include:
Name (Derek Walsh)
Title (CEO)
Phone Number (614-208-3917)
Address (48 Birchfield Court, Suite 314, Marlow, OH 43952)
Email (email@homebridle-example.com)
"NMLS" i.e. (NMLS 61947)
"Company NMLS" (Company NMLS 472815)

See above

```html
<!DOCTYPE html>
<html lang="en">
<head>
<meta charset="utf-8">
<title>HomeBridle — Derek Walsh Business Card</title>
<link rel="stylesheet" href="https://fonts.googleapis.com/css2?family=Montserrat:wght@200;300;400&display=swap">
<style>
  :root {
    --card-bg: #120f15;
    --ink: #ffffff;
    --ink-soft: #e9e7ec;
  }
  html, body {
    margin: 0;
    padding: 0;
    width: 1200px;
    height: 757px;
    overflow: hidden;
    background: var(--card-bg);
  }
  .business-card {
    position: relative;
    width: 1200px;
    height: 757px;
    background: var(--card-bg);
    color: var(--ink);
    font-family: "Montserrat", sans-serif;
    font-weight: 300;
  }
  .brand {
    position: absolute;
    left: 77px;
    top: 108px;
    width: 160px;
    text-align: center;
    font-size: 24px;
    font-weight: 300;
    letter-spacing: 0.5px;
    color: var(--ink);
  }
  .contact {
    position: absolute;
    right: 48px;
    top: 44px;
    text-align: right;
    color: var(--ink-soft);
  }
  .contact p {
    margin: 0;
    font-size: 23px;
    line-height: 34px;
    white-space: nowrap;
  }
  .contact .phone {
    font-size: 29px;
    line-height: 40px;
    margin-right: 9px;
  }
  .identity {
    position: absolute;
    left: 384px;
    top: 326px;
    width: 412px;
  }
  .identity .name {
    margin: 0;
    font-size: 73px;
    font-weight: 200;
    line-height: 84px;
    letter-spacing: 0.5px;
    white-space: nowrap;
  }
  .identity .title {
    margin: 0;
    text-align: right;
    font-size: 26px;
    font-weight: 400;
    line-height: 28px;
    letter-spacing: 0.5px;
  }
  .address {
    position: absolute;
    left: 0;
    right: 0;
    top: 678px;
    margin: 0;
    text-align: center;
    font-size: 28px;
    line-height: 38px;
    color: var(--ink-soft);
    white-space: nowrap;
  }
</style>
</head>
<body>
  <main class="business-card">
    <div class="brand">HomeBridle</div>

    <div class="contact">
      <p class="phone">(614-208-3917)</p>
      <p class="email">Email (email@homebridle-example.com)</p>
      <p class="nmls">"NMLS" i.e. (NMLS 61947)</p>
      <p class="company-nmls">"Company NMLS" (Company NMLS 472815)</p>
    </div>

    <div class="identity">
      <h1 class="name">Derek Walsh</h1>
      <p class="title">CEO</p>
    </div>

    <p class="address">Address (48 Birchfield Court, Suite 314, Marlow, OH 43952)</p>
  </main>
</body>
</html>
```